New Business Cards for Torvin Group

We need a new Business Card to compliment our new logo. We are a vibrant design, manufacture and install business providing recreation areas, public parks and Municipal spaces. We want business cards that are classy, modern and clean.

We have recently changed our logo, and are celebrating our 40th anniversary. We want business cards with a new modern design to reflect our status.

Target Market(s)

Customers

Contact Information for Business Card

We need all the details of our 3 offices as per the business card attached. Please disregard the old logo on the business card, the other three files show our new logo.

Requirements
Must have
• All info as per attached business card but with new logo.
Nice to have

```html
<!DOCTYPE html>
<html lang="en">
<head>
<meta charset="utf-8">
<title>Torvin Group Business Cards</title>
<link href="https://fonts.googleapis.com/css2?family=Arimo:wght@400;700&display=swap" rel="stylesheet">
<style>
  :root {
    --page: #e9e7e3;
    --paper: #ffffff;
    --charcoal: #3f3f41;
    --charcoal-dark: #2c2c2e;
    --red: #d6323a;
    --ink: #3a3a3c;
    --muted: #d9d9d9;
    --map: #58585b;
  }
  * { margin: 0; padding: 0; box-sizing: border-box; }
  html, body { width: 1200px; height: 780px; overflow: hidden; }
  body {
    background: var(--page);
    font-family: "Arimo", Arial, sans-serif;
    position: relative;
  }
  .card {
    position: absolute;
    width: 540px;
    height: 310px;
    top: 235px;
    overflow: hidden;
    box-shadow: 0 6px 18px rgba(0,0,0,.18);
  }
  /* Front */
  .card-front { left: 40px; background: var(--paper); }
  .front-top { position: absolute; left: 0; top: 0; width: 100%; height: 172px; }
  .brand {
    position: absolute; right: 30px; top: 34px;
    display: flex; align-items: center; gap: 10px;
  }
  .brand-dot { width: 34px; height: 34px; border-radius: 50%; background: var(--red); }
  .brand-name {
    font-weight: 700; font-size: 28px; color: var(--ink);
    letter-spacing: .5px; line-height: 1;
  }
  .person { position: absolute; left: 28px; top: 82px; }
  .person-name { font-weight: 700; font-size: 17px; color: var(--ink); }
  .person-role { font-size: 12px; color: var(--red); margin-top: 2px; }
  .person-contact { font-size: 11px; color: var(--ink); margin-top: 9px; line-height: 1.45; }
  .offices {
    position: absolute; left: 0; top: 172px; width: 100%; height: 96px;
    background: var(--charcoal);
    display: flex; gap: 20px; padding: 14px 24px 0;
  }
  .office { flex: 1; }
  .office-title { font-weight: 700; font-size: 12.5px; color: #fff; margin-bottom: 5px; }
  .office-line { font-size: 9px; color: var(--muted); line-height: 1.42; white-space: nowrap; }
  .web-strip {
    position: absolute; left: 0; top: 268px; width: 100%; height: 42px;
    background: var(--red);
    border-top: 3px solid #b9272e;
    display: flex; align-items: center; justify-content: center;
  }
  .web-strip span { color: #fff; font-size: 13px; letter-spacing: 2.5px; }
  /* Back */
  .card-back {
    left: 620px;
    background: radial-gradient(ellipse at 60% 40%, #555558 0%, var(--charcoal) 55%, var(--charcoal-dark) 100%);
  }
  .back-map {
    position: absolute; left: 120px; top: 30px; width: 380px; height: 250px;
    border-radius: 40% 50% 45% 55%;
    background: var(--map); opacity: .55;
  }
  .back-web {
    position: absolute; left: 22px; top: 155px;
    transform: translateY(-50%) rotate(90deg);
    transform-origin: left center;
    color: #cfcfcf; font-size: 12px; letter-spacing: 3px; white-space: nowrap;
    left: 40px; top: 70px; transform: rotate(90deg); transform-origin: left top;
  }
  .back-brand {
    position: absolute; left: 170px; top: 128px;
    display: flex; align-items: center; gap: 12px;
  }
  .back-brand .brand-dot { width: 44px; height: 44px; background: #fff; }
  .back-brand .brand-name { color: #fff; font-size: 36px; }
</style>
</head>
<body>
  <section class="card card-front">
    <div class="front-top">
      <div class="brand">
        <span class="brand-dot"></span>
        <span class="brand-name">TORVIN GROUP</span>
      </div>
      <div class="person">
        <div class="person-name">Marek Delano</div>
        <div class="person-role">Managing Partner</div>
        <div class="person-contact">
          Mobile No: +971 (0)50 384 7162<br>
          Email: marek@torvingroup.com
        </div>
      </div>
    </div>
    <div class="offices">
      <div class="office">
        <div class="office-title">Head Office</div>
        <div class="office-line">P.O. Box: 41852 Abu Dhabi, U.A.E.</div>
        <div class="office-line">Tel No: +971 (0)2 5137290</div>
        <div class="office-line">Fax No: +971 (0)2 5137291</div>
        <div class="office-line">Email: sales@torvingroup.com</div>
      </div>
      <div class="office">
        <div class="office-title">Dubai Office</div>
        <div class="office-line">P.O. Box: 270614 Dubai, U.A.E.</div>
        <div class="office-line">Tel No: +971 (0)4 3826405</div>
        <div class="office-line">Fax No: +971 (0)4 3826406</div>
        <div class="office-line">Email: sales@torvingroup.com</div>
      </div>
      <div class="office">
        <div class="office-title">Qatar Office</div>
        <div class="office-line">P.O. Box: 58230 Doha, Qatar</div>
        <div class="office-line">Tel No: +974 44710386</div>
        <div class="office-line">Fax No: +974 44710387</div>
        <div class="office-line">Email: sales@torvingroup.com</div>
      </div>
    </div>
    <div class="web-strip"><span>www.torvingroup.com</span></div>
  </section>

  <section class="card card-back">
    <div class="back-map" role="img" aria-label="Faint world map background"></div>
    <div class="back-web">www.torvingroup.com</div>
    <div class="back-brand">
      <span class="brand-dot"></span>
      <span class="brand-name">TORVIN GROUP</span>
    </div>
  </section>
</body>
</html>
```